A4 Childcare Spring Special Flyer

Crestwell Learning is a registered training organisation (RTO) Toid No. 47318, based in Blackburn, Victoria. We are a market leader in Professional development courses both accredited and non accredited, in order for you to maintain currency in your profession.

We need a flyer for a childcare specific spring special. The special is to offer a $50 VOLM gift card and 50% of your second training session. Conditions apply*

The training sessions available are the NEW childcare specific course: HLTAID004 Provide an emergency first aid response in an education and care setting and HLTAID003 Provide First Aid, HLTAID001 Provide Cardiopulmonary Resuscitation (CPR), 22024VIC Course in emergency management of asthma in the workplace
and 22099VIC Course in First Aid Management of Anaphylaxis.
We provide a flexible, cost effective and reliable service.
We have training locations available in Blackburn, Preston, Narre Warren and Mornington and can also provide onsite training.

We can also provide education and PRIVOS regulation consultation to the childcare provider.

Must use company logo, include phone number: (03) 5127 6481, website: www.crestwelllearning.com.au, email: marapenn@crestwelllearning.com.au

(Note that a letter with more detail will be attached with this flyer, therefore, with that in mind; use that information as desired).

The final product should be as childcare like as possible whilst also keeping our company colors (same as logo). We would also like for this flyer to stand out and be appealing to the recipient as this flyer is to gain potential clients, with emphasis on the HLTAID004 Course
Updates

Just need to update the qualifications: In the design brief I mentioned that the course; HLTAID001 Provide CPR and Asthma & Anaphyalxis.. Can this please be changed to HLTAID001 Provide Cardiopulmonary Resuscitation (CPR) And 22024VIC Course in emergency management of asthma in the workplace And 22099VIC Course in First Aid Management of Anaphylaxis (They are all singular courses) Apoligies!

Target Market(s)

Childcare centres, Out of school hours providers, pre-schools

Industry/Entity Type

Childcare

Font styles to use
Decorative

Colors
ffcf3e
f37123
faa54b

Requirements
Must have
• Company Logo
phone number
website
email
Registered Training Organisation
TOID: 47318

```html
<!DOCTYPE html>
<html lang="en">
<head>
<meta charset="utf-8">
<title>Crestwell Learning – Childcare Spring Special</title>
<link rel="stylesheet" href="https://fonts.googleapis.com/css2?family=Alfa+Slab+One&family=Didact+Gothic&family=Roboto+Condensed:wght@700&family=Oswald:wght@600&display=swap">
<style>
  :root{
    --orange:#f37123;
    --orange-deep:#ee5a24;
    --orange-soft:#faa54b;
    --yellow:#ffcf3e;
    --green:#4db848;
    --grey:#4a4a4a;
    --ink:#2b2b2b;
    --paper:#ffffff;
    --peach:#f7c9a0;
  }
  *{margin:0;padding:0;box-sizing:border-box}
  html,body{width:1028px;height:1200px;overflow:hidden;background:var(--paper)}
  .flyer{position:relative;width:1028px;height:1200px;overflow:hidden;background:var(--paper);font-family:"Didact Gothic",sans-serif;color:var(--ink)}
  .shapes{position:absolute;left:0;top:0;width:1028px;height:1200px}
  .headline{position:absolute;left:50px;top:18px;font-family:"Alfa Slab One",serif;font-weight:400;font-size:60px;line-height:63px;letter-spacing:1.5px;color:var(--orange-deep)}
  .brand{position:absolute;left:704px;top:43px;width:200px;text-align:center}
  .brand-dot{width:110px;height:110px;border-radius:50%;background:var(--orange);margin:0 auto 27px}
  .brand-name{font-size:30px;line-height:29px;color:var(--grey)}
  .toid{position:absolute;left:832px;top:251px;width:80px;text-align:center;font-family:"Roboto Condensed",sans-serif;font-weight:700;font-size:12px;line-height:14px;letter-spacing:3px;color:var(--ink)}
  .courses-title{position:absolute;left:43px;top:633px;font-family:"Oswald",sans-serif;font-weight:600;font-size:26px;line-height:32px;letter-spacing:.5px;color:var(--orange);border-bottom:2px solid var(--orange-soft)}
  .course-list{position:absolute;left:43px;top:675px;list-style:none;font-size:21px;line-height:31px;letter-spacing:1.3px;white-space:nowrap;color:var(--ink)}
  .bubble-text{position:absolute;text-align:center;color:#fff;white-space:nowrap}
  .bubble-text span{display:block}
  .bubble-locations{left:71px;top:868px;width:260px;font-size:17px;line-height:20px}
  .bubble-consult{left:340px;top:884px;width:244px;font-size:16px;line-height:18.5px}
  .bubble-service{left:592px;top:892px;width:160px;font-size:17px;line-height:19.5px}
  .badge-text{position:absolute;text-align:center;color:#fff;font-family:"Roboto Condensed",sans-serif;font-weight:700;white-space:nowrap}
  .offer-text{left:759px;top:614px;width:180px}
  .offer-big{font-size:38px;line-height:42px}
  .offer-small{font-size:19px;line-height:24px;margin-top:4px}
  .gift-text{left:865px;top:872px;width:150px}
  .gift-big{font-size:44px;line-height:48px}
  .gift-small{font-size:20px;line-height:25px;margin-top:2px}
  .call{position:absolute;left:43px;top:1048px;font-family:"Roboto Condensed",sans-serif;font-weight:700;font-size:57px;line-height:62px;color:var(--ink);white-space:nowrap}
  .contact{position:absolute;left:43px;top:1111px;font-family:Arial,Helvetica,sans-serif;font-size:22px;line-height:27px;color:var(--ink);white-space:nowrap}
  .contact .web{padding-left:3px}
</style>
</head>
<body>
<main class="flyer">
  <svg class="shapes" viewBox="0 0 1028 1200">
    <defs>
      <clipPath id="photo-clip">
        <path d="M0,330 C200,250 420,240 560,270 C720,300 880,300 1028,262 L1028,480 C900,580 760,615 560,600 C400,590 200,580 0,605 Z"/>
      </clipPath>
      <filter id="lift" x="-15%" y="-15%" width="130%" height="140%">
        <feDropShadow dx="0" dy="3" stdDeviation="3" flood-color="#000" flood-opacity=".35"/>
      </filter>
      <linearGradient id="g-asthma" x1="0" y1="0" x2="1" y2="1"><stop offset="0" stop-color="#c9d3da"/><stop offset="1" stop-color="#e8c8a8"/></linearGradient>
      <linearGradient id="g-class" x1="0" y1="0" x2="1" y2="1"><stop offset="0" stop-color="#d9d2c4"/><stop offset="1" stop-color="#b89b7c"/></linearGradient>
      <linearGradient id="g-care" x1="0" y1="0" x2="1" y2="1"><stop offset="0" stop-color="#c8a17e"/><stop offset="1" stop-color="#e5b8b4"/></linearGradient>
      <linearGradient id="g-play" x1="0" y1="0" x2="1" y2="1"><stop offset="0" stop-color="#e0513a"/><stop offset="1" stop-color="#e77f9a"/></linearGradient>
      <linearGradient id="g-cpr" x1="0" y1="0" x2="1" y2="1"><stop offset="0" stop-color="#9a2a24"/><stop offset="1" stop-color="#e7d2c6"/></linearGradient>
      <linearGradient id="g-blocks" x1="0" y1="0" x2="1" y2="0"><stop offset="0" stop-color="#f5a04a"/><stop offset=".35" stop-color="#59b5e6"/><stop offset=".7" stop-color="#e6463a"/><stop offset="1" stop-color="#8a62c4"/></linearGradient>
    </defs>

    <g clip-path="url(#photo-clip)">
      <rect role="img" aria-label="Photo: young child using an asthma inhaler" x="0" y="230" width="345" height="227" fill="url(#g-asthma)"/>
      <rect role="img" aria-label="Photo: educators with a group of smiling preschool children" x="0" y="460" width="345" height="160" fill="url(#g-class)"/>
      <rect role="img" aria-label="Photo: carer applying a bandage to a girl's knee" x="348" y="230" width="331" height="390" fill="url(#g-care)"/>
      <rect role="img" aria-label="Photo: happy children cheering in a colourful play room" x="682" y="230" width="346" height="227" fill="url(#g-play)"/>
      <rect role="img" aria-label="Photo: gloved hands practising CPR on a training manikin" x="682" y="460" width="346" height="160" fill="url(#g-cpr)"/>
    </g>

    <path class="wave-top" fill="var(--orange)" d="M0,298 C200,218 420,212 560,242 C720,276 880,282 1028,240 L1028,262 C880,300 720,300 560,270 C420,240 200,250 0,332 Z"/>
    <path class="wave-bottom" fill="var(--orange-deep)" d="M0,605 C200,580 400,590 560,600 C760,615 900,580 1028,480 L1028,578 C880,640 700,662 500,658 C300,652 150,625 0,620 Z"/>

    <path stroke="var(--peach)" stroke-width="5" fill="none" d="M897,752 L968,805 M968,833 L925,862"/>

    <g filter="url(#lift)">
      <ellipse cx="201" cy="943" rx="145" ry="89" fill="var(--orange)" stroke="#fff" stroke-width="5"/>
      <ellipse cx="462" cy="940" rx="127" ry="81" fill="var(--orange-deep)" stroke="#fff" stroke-width="5"/>
      <ellipse cx="672" cy="941" rx="97" ry="67" fill="var(--grey)" stroke="#fff" stroke-width="5"/>
    </g>

    <g filter="url(#lift)">
      <polygon class="star-offer" transform="translate(849,660) scale(1.05) translate(-100,-100)" fill="var(--green)" stroke="#fff" stroke-width="5" stroke-linejoin="round" points="200,100 181.1,121.7 186.6,150 159.4,159.4 150,186.6 121.7,181.1 100,200 78.3,181.1 50,186.6 40.6,159.4 13.4,150 18.9,121.7 0,100 18.9,78.3 13.4,50 40.6,40.6 50,13.4 78.3,18.9 100,0 121.7,18.9 150,13.4 159.4,40.6 186.6,50 181.1,78.3"/>
      <polygon class="star-gift" transform="translate(940,928) scale(0.86) translate(-100,-100)" fill="var(--orange-deep)" stroke="#fff" stroke-width="6" stroke-linejoin="round" points="200,100 181.1,121.7 186.6,150 159.4,159.4 150,186.6 121.7,181.1 100,200 78.3,181.1 50,186.6 40.6,159.4 13.4,150 18.9,121.7 0,100 18.9,78.3 13.4,50 40.6,40.6 50,13.4 78.3,18.9 100,0 121.7,18.9 150,13.4 159.4,40.6 186.6,50 181.1,78.3"/>
    </g>

    <rect role="img" aria-label="Illustration: colourful wooden toy blocks spelling CHILD CARE" x="578" y="1028" width="389" height="133" rx="6" fill="url(#g-blocks)" opacity=".85"/>
  </svg>

  <h1 class="headline">making YOU<br>the future of<br>health care</h1>

  <div class="brand">
    <div class="brand-dot"></div>
    <div class="brand-name">crestwell<br>learning</div>
  </div>
  <div class="toid">TOID<br>47318</div>

  <div class="badge-text offer-text">
    <div class="offer-big">50% OFF</div>
    <div class="offer-small">Your Second<br>Training Session</div>
  </div>

  <h2 class="courses-title">COURSES:</h2>
  <ul class="course-list">
    <li>HLTAID003 Provide First Aid</li>
    <li>HLTAID001 Provide Cardiopulmonary Resuscitation (CPR)</li>
    <li>22099VIC Course in First Aid Management of Anaphylaxis</li>
    <li>22024VIC Course in emergency management of asthma in the workplace</li>
    <li>HLTAID004 Provide an emergency first aid response in an education and care setting</li>
  </ul>

  <p class="bubble-text bubble-locations"><span>We have training</span><span>locations available</span><span>in Blackburn, Preston,</span><span>Narre Warren and</span><span>Mornington and can</span><span>also provide</span><span>onsite training</span></p>
  <p class="bubble-text bubble-consult"><span>We can also</span><span>provide education</span><span>and</span><span>PRIVOS regulation</span><span>consultation to the</span><span>childcare provider</span></p>
  <p class="bubble-text bubble-service"><span>We provide</span><span>flexible,</span><span>cost effective</span><span>and reliable</span><span>service</span></p>

  <div class="badge-text gift-text">
    <div class="gift-big">$50</div>
    <div class="gift-small">VOLM<br>Gift Card</div>
  </div>

  <p class="call">Call (03) 5127 6481</p>
  <p class="contact">email: marapenn@crestwelllearning.com.au<br><span class="web">website: www.crestwelllearning.com.au</span></p>
</main>
</body>
</html>
```